Please design a business card with my current logo (attached below).

I have some specifics that must be included:
1. I want the emphasis on Accredited Legacy Home Transfer Advisor.
2. Leave room for my picture.
3. Company name, address, phone numbers and email address.
4. My BRE# should be placed under my name.

```html
<!DOCTYPE html>
<html lang="en">
<head>
<meta charset="utf-8">
<title>Mara Delling – Business Card</title>
<link href="https://fonts.googleapis.com/css2?family=Cinzel:wght@600&family=Libre+Baskerville:wght@400;700&display=swap" rel="stylesheet">
<style>
  :root {
    --bg: #e9e6e1;
    --card: #ffffff;
    --ink: #2b2b2b;
    --red: #c0202a;
    --rule: #9a9a9a;
    --photo-a: #d9d4cd;
    --photo-b: #5a5a5e;
  }
  * { box-sizing: border-box; margin: 0; padding: 0; }
  html, body { width: 1200px; height: 784px; overflow: hidden; }
  body {
    background: var(--bg);
    position: relative;
    font-family: "Libre Baskerville", "Times New Roman", serif;
    color: var(--ink);
  }
  .card {
    position: absolute;
    width: 560px;
    height: 320px;
    background: var(--card);
    box-shadow: 0 2px 8px rgba(0,0,0,0.12);
    overflow: hidden;
  }
  .card--front { left: 320px; top: 48px; }
  .card--back { left: 320px; top: 408px; }

  .brand {
    display: flex;
    align-items: center;
    justify-content: center;
    gap: 14px;
    font-family: "Cinzel", "Times New Roman", serif;
    font-weight: 600;
    color: var(--ink);
    white-space: nowrap;
  }
  .brand__mark { background: var(--red); flex: none; }
  .card--front .brand { height: 100%; font-size: 54px; }
  .card--front .brand__mark { width: 30px; height: 30px; }

  .card--back .brand {
    position: absolute; left: 0; right: 0; top: 44px;
    font-size: 34px; gap: 10px;
  }
  .card--back .brand__mark { width: 18px; height: 18px; }

  .title-band {
    position: absolute; left: 0; right: 0; top: 120px;
    height: 22px;
    background: var(--red);
    color: #fff;
    font-weight: 700;
    font-size: 11.5px;
    letter-spacing: 2.4px;
    text-align: center;
    line-height: 22px;
    white-space: nowrap;
  }

  .portrait {
    position: absolute; left: 36px; top: 160px;
    width: 118px; height: 140px;
    border: 2px solid var(--ink);
    padding: 4px;
  }
  .portrait__fill {
    width: 100%; height: 100%;
    background: linear-gradient(180deg, var(--photo-a) 0%, var(--photo-a) 45%, var(--photo-b) 100%);
  }

  .agent { position: absolute; left: 170px; top: 176px; }
  .agent__name { color: var(--red); font-size: 19px; white-space: nowrap; }
  .agent__licence { font-size: 12px; margin-top: 4px; }

  .divider {
    position: absolute; left: 308px; top: 160px;
    width: 1px; height: 96px; background: var(--rule);
  }

  .contacts {
    position: absolute; left: 322px; top: 160px;
    list-style: none; font-size: 12px;
  }
  .contacts li { display: flex; align-items: center; gap: 7px; height: 22px; white-space: nowrap; }
  .contacts svg { width: 14px; height: 14px; fill: var(--red); flex: none; }
</style>
</head>
<body>
  <section class="card card--front" aria-label="Card front">
    <div class="brand"><span class="brand__mark"></span>Mara Delling</div>
  </section>

  <section class="card card--back" aria-label="Card back">
    <div class="brand"><span class="brand__mark"></span>Mara Delling</div>
    <div class="title-band">Accredited Legacy Home Transfer Advisor</div>

    <div class="portrait"><div class="portrait__fill" role="img" aria-label="Portrait photo of the agent"></div></div>

    <div class="agent">
      <p class="agent__name">Mara Delling</p>
      <p class="agent__licence">BRE#40271856</p>
    </div>

    <div class="divider"></div>

    <ul class="contacts">
      <li><svg viewBox="0 0 24 24"><path d="M6.6 10.8a15 15 0 0 0 6.6 6.6l2.2-2.2c.3-.3.7-.4 1-.2 1.1.4 2.3.6 3.6.6.6 0 1 .4 1 1V20c0 .6-.4 1-1 1A17 17 0 0 1 3 4c0-.6.4-1 1-1h3.5c.6 0 1 .4 1 1 0 1.3.2 2.5.6 3.6.1.3 0 .7-.2 1z"/></svg>(555) 014-2961</li>
      <li><svg viewBox="0 0 24 24"><path d="M2 5h20v14H2z M3.5 6.5 12 13l8.5-6.5" fill="none" stroke="#c0202a" stroke-width="2"/></svg>hello@maradelling.com</li>
      <li><svg viewBox="0 0 24 24"><g fill="none" stroke="#c0202a" stroke-width="1.8"><circle cx="12" cy="12" r="9.5"/><ellipse cx="12" cy="12" rx="4" ry="9.5"/><path d="M2.5 12h19M4 7h16M4 17h16"/></g></svg>www.maradelling.com</li>
      <li><svg viewBox="0 0 24 24"><path d="M12 3 2 12h3v9h5v-6h4v6h5v-9h3z"/></svg>4172 Willow Road, Suite 12,</li>
    </ul>
  </section>
</body>
</html>
```